Venturo Australia
Project: Venturo Australia - Stationary
Venturo Australia - Stationary - Travel
Venturo Australia - Stationary
Bright & Fun-filled
Giulia Rossabene
Director
17 Harlow Crescent, Bramwick Heights, Western Australia 6012
giulia@venturoaustralia.example
www.venturoaustralia.example

```html
<!DOCTYPE html>
<html lang="en">
<head>
<meta charset="utf-8">
<title>Venturo Australia – Stationery</title>
<link href="https://fonts.googleapis.com/css2?family=Oswald:wght@400;600&family=Roboto+Condensed:wght@400;700&display=swap" rel="stylesheet">
<style>
:root{
  --blue:#2a8fd0;
  --teal:#1fb3c8;
  --teal-deep:#1690ae;
  --red:#e8502c;
  --amber:#f5a623;
  --green:#1e9f5a;
  --lime:#45b649;
  --ink:#3a3a3a;
  --grey:#8a8a8a;
  --rule:#e3e6ea;
  --paper:#ffffff;
}
*{margin:0;padding:0;box-sizing:border-box}
html,body{width:1200px;height:802px;overflow:hidden;background:#fff}
body{position:relative;font-family:"Roboto Condensed",Arial,sans-serif;color:var(--ink)}

.card{position:absolute;left:101px;width:403px;height:240px;border-radius:10px;overflow:hidden}
.card--front{top:132px;background:var(--paper);border:1px solid var(--rule);box-shadow:0 4px 10px rgba(0,0,0,.12)}
.card--back{top:432px;box-shadow:0 4px 10px rgba(0,0,0,.15)}

.brand{font-family:"Oswald",Arial,sans-serif;font-weight:600;color:var(--blue);display:flex;align-items:center;gap:7px;line-height:1;white-space:nowrap}
.brand__dot{width:12px;height:12px;border-radius:50%;background:var(--red);flex:none}

.card--front .brand{position:absolute;left:26px;top:84px;width:186px;font-size:23px}

.divider{position:absolute;left:222px;top:36px;width:1px;height:128px;background:var(--rule)}
.contact{position:absolute;left:232px;top:34px;width:165px;list-style:none;font-size:8.5px;color:var(--ink)}
.contact li{display:flex;align-items:center;gap:6px;height:16px;white-space:nowrap}
.contact .icon{width:10px;height:10px;border-radius:50%;background:var(--red);flex:none}
.contact li.address{height:auto;align-items:flex-start;margin-top:2px;line-height:1.3;white-space:normal}

.person{position:absolute;left:0;width:222px;top:170px;text-align:center}
.person__name{font-family:"Oswald",Arial,sans-serif;font-weight:600;font-size:16px;color:var(--red);letter-spacing:.5px;text-transform:uppercase}
.person__role{font-size:8px;letter-spacing:5px;color:var(--grey);text-transform:uppercase;margin-top:2px}

.colour-bar{position:absolute;left:0;right:0;bottom:0;height:8px;display:flex}
.colour-bar span{flex:1}
.colour-bar span:nth-child(1){background:var(--blue)}
.colour-bar span:nth-child(2){background:var(--teal)}
.colour-bar span:nth-child(3){background:var(--red)}
.colour-bar span:nth-child(4){background:var(--amber)}
.colour-bar span:nth-child(5){background:var(--green)}
.colour-bar span:nth-child(6){background:var(--lime)}

.card__pattern{position:absolute;inset:0;background:radial-gradient(circle at 50% 45%,var(--teal) 0%,var(--teal-deep) 100%)}
.card--back .brand{position:absolute;left:0;right:0;top:96px;justify-content:center;font-size:28px;color:#fff}
.card__web{position:absolute;left:0;right:0;bottom:20px;text-align:center;color:#fff;font-size:8px;letter-spacing:3px}

.letterhead{position:absolute;left:612px;top:43px;width:504px;height:706px;background:var(--paper);border:1px solid var(--rule);box-shadow:0 4px 12px rgba(0,0,0,.12);overflow:hidden}
.letterhead .brand{position:absolute;left:36px;top:34px;font-size:22px}
.letterhead__meta{position:absolute;left:36px;top:118px;width:140px}
.letterhead__meta span{display:block;height:1px;background:var(--rule);margin-bottom:22px}
.letterhead__body{position:absolute;left:36px;right:36px;top:230px}
.letterhead__body span{display:block;height:1px;background:var(--rule);margin-bottom:21px}
.letterhead__footer{position:absolute;left:0;right:0;bottom:22px;text-align:center;font-size:6.5px;line-height:1.45;color:var(--ink)}
.letterhead .colour-bar{height:7px}
</style>
</head>
<body>

<section class="card card--front" aria-label="Business card front">
  <div class="brand"><span class="brand__dot"></span>Venturo Australia</div>
  <div class="divider"></div>
  <ul class="contact">
    <li><span class="icon"></span>+61 08 5550 1234</li>
    <li><span class="icon"></span>+61 04 5550 9876</li>
    <li><span class="icon"></span>giulia@venturoaustralia.example</li>
    <li><span class="icon"></span>social/venturoaustralia</li>
    <li><span class="icon"></span>chat: giulia.venturo</li>
    <li><span class="icon"></span>www.venturoaustralia.example</li>
    <li class="address"><span class="icon"></span>17 Harlow Crescent, Bramwick Heights,<br>Western Australia 6012</li>
  </ul>
  <div class="person">
    <div class="person__name">Giulia Rossabene</div>
    <div class="person__role">Director</div>
  </div>
  <div class="colour-bar"><span></span><span></span><span></span><span></span><span></span><span></span></div>
</section>

<section class="card card--back" aria-label="Business card back">
  <div class="card__pattern" role="img" aria-label="Teal background with faint repeating continent pattern"></div>
  <div class="brand">Venturo Australia</div>
  <div class="card__web">www.venturoaustralia.example</div>
</section>

<section class="letterhead" aria-label="Letterhead">
  <div class="brand"><span class="brand__dot"></span>Venturo Australia</div>
  <div class="letterhead__meta"><span></span><span></span><span></span></div>
  <div class="letterhead__body">
    <span></span><span></span><span></span><span></span><span></span><span></span><span></span><span></span><span></span><span></span><span></span><span></span><span></span><span></span><span></span>
  </div>
  <div class="letterhead__footer">
    17 Harlow Crescent, Bramwick Heights<br>
    Western Australia 6012<br>
    +61 08 5550 1234<br>
    +61 04 5550 9876<br>
    social/venturoaustralia<br>
    www.venturoaustralia.example
  </div>
  <div class="colour-bar"><span></span><span></span><span></span><span></span><span></span><span></span></div>
</section>

</body>
</html>
```